Hal's Remedies Business Card Design Project

I need a business card designed for my pharmacy Hal's Remedies. I would like just the logo on one side, maybe with black background and white lettering. The other side I would also like to include my logo which is attached. Also, please include my name and the following information:
Hal Norwick Owner/Pharm D.
Business address is 7163 N Birch Rd Sioux Falls, SD 57291.
Phone number is 605-318-6027 and fax # is 605-318-6031.
my email address is hal@halsremedies.example.
My website is www.halsremedies.example.
My business hours are Monday-Friday 8am-7 pm. Saturday 8am-12 pm. Sunday Closed.
I would like the design to include my logo colors, black, white, and neon green. Silver may be added as a highlight. Thanks.
Pharmacy
See above in product description

```html
<!DOCTYPE html>
<html lang="en">
<head>
<meta charset="utf-8">
<title>Hal's Remedies – Business Card</title>
<link href="https://fonts.googleapis.com/css2?family=Open+Sans:wght@400;600;700&family=Satisfy&display=swap" rel="stylesheet">
<style>
  :root {
    --stage: #505050;
    --ink: #1a1a1a;
    --text: #2b2b2b;
    --neon: #8cc63f;
    --navy: #1d3346;
    --teal-light: #2f5d78;
    --teal-dark: #15293a;
    --white: #ffffff;
    --silver: #d9dde0;
  }
  * { margin: 0; padding: 0; box-sizing: border-box; }
  html, body { width: 1200px; height: 820px; overflow: hidden; }
  body {
    background: var(--stage);
    font-family: "Open Sans", Arial, sans-serif;
    position: relative;
  }
  .card {
    position: absolute;
    top: 258px;
    width: 471px;
    height: 270px;
    border-radius: 22px;
    overflow: hidden;
  }
  .card-front { left: 117px; background: var(--white); }
  .card-back {
    left: 629px;
    background: radial-gradient(ellipse at 50% 40%, var(--teal-light) 0%, #214660 45%, var(--teal-dark) 100%);
  }

  /* front: brand block */
  .brand-front {
    position: absolute;
    left: 30px; top: 140px;
    width: 205px;
    display: flex; align-items: center; justify-content: center; gap: 8px;
  }
  .brand-dot { width: 14px; height: 14px; border-radius: 50%; background: var(--neon); flex: none; }
  .brand-front .brand-name {
    font-size: 25px; font-weight: 700; color: var(--ink); letter-spacing: -0.5px; white-space: nowrap;
  }
  .divider-front {
    position: absolute; left: 243px; top: 68px;
    width: 1px; height: 140px; background: #d5d5d5;
  }

  /* front: contact */
  .contact { position: absolute; left: 275px; top: 46px; color: var(--text); }
  .contact .person { font-size: 18px; font-weight: 400; color: var(--ink); line-height: 22px; }
  .contact .role { font-size: 13.5px; color: var(--neon); line-height: 20px; }
  .contact .address { margin-top: 6px; font-size: 12px; line-height: 18px; }
  .contact-list { list-style: none; margin-top: 14px; font-size: 12px; }
  .contact-list li { display: flex; align-items: center; gap: 8px; height: 19px; }
  .contact-list svg { width: 10px; height: 10px; flex: none; }
  .contact-list li.phone { padding-left: 0; }
  .contact-list .accent { color: var(--neon); }

  /* front: footer band */
  .footer-wave { position: absolute; left: 0; bottom: 0; width: 471px; height: 50px; }
  .hours {
    position: absolute; left: 0; bottom: 9px; width: 100%;
    text-align: center; color: var(--white); font-size: 11.5px; font-weight: 600;
  }

  /* back */
  .brand-back {
    position: absolute; left: 72px; top: 100px;
    display: flex; align-items: center;
  }
  .brand-back .brand-dot { width: 30px; height: 30px; margin-right: 58px; background: var(--silver); }
  .divider-back { width: 1px; height: 60px; background: var(--silver); margin-right: 16px; }
  .brand-back .brand-name {
    font-size: 29px; font-weight: 600; color: var(--white); line-height: 32px; letter-spacing: -0.3px;
  }
  .brand-back .tagline {
    font-family: "Satisfy", cursive; font-size: 15px; color: var(--silver); line-height: 20px;
  }
  .web-back {
    position: absolute; left: 0; top: 214px; width: 100%;
    text-align: center; color: var(--white); font-size: 13.5px;
  }
</style>
</head>
<body>

  <section class="card card-front">
    <div class="brand-front">
      <span class="brand-dot"></span>
      <span class="brand-name">Hal's Remedies</span>
    </div>
    <div class="divider-front"></div>

    <div class="contact">
      <p class="person">Hal Norwick</p>
      <p class="role">Owner/Pharm D</p>
      <p class="address">7163 N Birch Rd Sioux Falls,<br>SD 57291.</p>
      <ul class="contact-list">
        <li>
          <svg viewBox="0 0 10 10"><path d="M2 0.5 L4 2.5 L3 3.8 Q4.5 6 6.2 7 L7.5 6 L9.5 8 L8 9.5 Q3 9 0.5 2 Z" fill="var(--neon)"/></svg>
          605-318-6027
        </li>
        <li>
          <svg viewBox="0 0 10 10"><rect x="0.5" y="3" width="9" height="6.5" fill="var(--neon)"/><rect x="2.5" y="0.5" width="5" height="3.5" fill="var(--neon)"/></svg>
          605-318-6031
        </li>
        <li>
          <svg viewBox="0 0 10 10"><rect x="0.5" y="2" width="9" height="6.5" fill="var(--neon)"/><path d="M0.8 2.3 L5 5.8 L9.2 2.3" stroke="var(--white)" stroke-width="1" fill="none"/></svg>
          hal@halsremedies.example
        </li>
        <li>
          <svg viewBox="0 0 10 10"><circle cx="5" cy="5" r="4.3" fill="none" stroke="var(--neon)" stroke-width="1.2"/><path d="M0.8 5 H9.2 M5 0.8 Q2.5 5 5 9.2 M5 0.8 Q7.5 5 5 9.2" stroke="var(--neon)" stroke-width="0.9" fill="none"/></svg>
          <span>www.<span class="accent">halsremedies</span>.example</span>
        </li>
      </ul>
    </div>

    <svg class="footer-wave" viewBox="0 0 471 50" preserveAspectRatio="none" aria-hidden="true">
      <path d="M0 20 C120 0 250 2 340 10 C400 15 440 8 471 2 L471 50 L0 50 Z" fill="var(--navy)"/>
      <path d="M0 16 C120 -3 250 0 340 7 C400 12 440 5 471 -1" fill="none" stroke="var(--neon)" stroke-width="3"/>
      <path d="M0 19 C120 1 250 3 340 10 C400 14 440 7 471 1" fill="none" stroke="#cfe8a8" stroke-width="1"/>
    </svg>
    <p class="hours">business hours are Monday-Friday 8am-7 pm. Saturday 8am-12 pm. Sunday Closed.</p>
  </section>

  <section class="card card-back">
    <div class="brand-back">
      <span class="brand-dot"></span>
      <span class="divider-back"></span>
      <div>
        <p class="brand-name">Hal's Remedies</p>
        <p class="tagline">7163 N. Birch Rd. Sioux Falls, SD</p>
      </div>
    </div>
    <p class="web-back">www.halsremedies.example</p>
  </section>

</body>
</html>
```